Design uplift of Quillabend.com site

The site needs to be fast and responsive down to mobile.
Needs to use the supplied Video as the homepage background.
Needs to use Generate Press as the theme - Site theme to be a child theme of Generate Press.
Needs to have a button above the fold for an offer of a free email course on how to set up a medical software project.
Needs to use the Quillabend logo. This logo has been trademarked.

The existing site is at: www.quillabend.com

```html
<!DOCTYPE html>
<html lang="en">
<head>
<meta charset="utf-8">
<title>Quillabend – Custom Software Development</title>
<link rel="stylesheet" href="https://fonts.googleapis.com/css2?family=Poppins:wght@400;500;600&display=swap">
<style>
:root{
  --blue:#139fe0;
  --blue-dark:#0b86c4;
  --ink:#1d2330;
  --text:#3a3f4a;
  --muted:#6b717c;
  --pale:#eef8fc;
  --white:#ffffff;
  --footer:#121212;
  --rule:#e6e9ee;
}
*{box-sizing:border-box;margin:0;padding:0}
html,body{width:1200px;height:3231px;overflow:hidden}
body{position:relative;font-family:'Poppins',sans-serif;color:var(--text);background:var(--white)}
.abs{position:absolute}
a{color:inherit;text-decoration:none}

/* top bar */
.topbar{left:0;top:0;width:1200px;height:40px;background:var(--blue)}
.search{left:517px;top:6px;width:207px;height:29px;border-radius:15px;background:#1a8fc8;color:#dcefff;font-size:12px;line-height:29px;padding-left:13px}
.search svg{position:absolute;right:10px;top:7px}
.topbar .sep{top:8px;width:1px;height:24px;background:rgba(255,255,255,.6)}
.top-contact{top:0;height:40px;line-height:40px;color:#fff;font-size:15px;font-weight:500;display:flex;align-items:center;gap:8px;white-space:nowrap}

/* nav */
.nav{left:0;top:40px;width:1200px;height:79px;background:#fff;box-shadow:0 1px 0 #eee}
.brand{display:flex;align-items:center;gap:10px;font-weight:600;font-size:28px;color:var(--ink);white-space:nowrap}
.brand .mark{width:40px;height:40px;border-radius:50%;background:var(--blue)}
.menu{top:0;height:79px;display:flex;align-items:center;font-size:14px;font-weight:500;color:var(--ink)}
.menu .item{position:absolute;white-space:nowrap}
.menu .active{color:var(--blue)}
.menu .active::after{content:"";position:absolute;left:0;right:0;top:38px;height:3px;background:var(--blue)}
.btn{display:inline-flex;align-items:center;justify-content:center;gap:5px;border-radius:20px;font-weight:600;font-size:14px;color:#fff;background:var(--blue);white-space:nowrap}
.btn-outline{background:#fff;color:var(--blue);border:2px solid var(--blue)}
.arrow{width:11px;height:11px;border-radius:50%;background:currentColor;position:relative;display:inline-block}
.arrow::after{content:"";position:absolute;left:3px;top:3px;border:2.5px solid transparent;border-left:4px solid var(--blue)}
.btn-outline .arrow::after{border-left-color:#fff}

/* media areas */
.media{overflow:hidden}
.media::after{content:"";position:absolute;inset:0;background:linear-gradient(180deg,rgba(255,255,255,.06),rgba(0,0,0,.12))}

/* hero */
.hero{left:0;top:119px;width:1200px;height:656px;
  background:
    radial-gradient(ellipse 420px 260px at 78% 30%,rgba(90,190,220,.45),transparent 70%),
    radial-gradient(ellipse 520px 240px at 55% 75%,rgba(130,170,230,.55),transparent 70%),
    radial-gradient(ellipse 300px 300px at 35% 35%,rgba(60,110,180,.6),transparent 70%),
    linear-gradient(160deg,#0f2a55 0%,#1c4a8a 45%,#0d2148 100%)}
.hero::before{content:"";position:absolute;inset:0;background:linear-gradient(90deg,rgba(5,15,40,.45),rgba(5,15,40,0) 55%)}
.play{left:100px;top:326px;width:100px;height:100px;border-radius:50%;background:rgba(210,215,225,.55);display:flex;align-items:center;justify-content:center}
.play .inner{width:72px;height:72px;border-radius:50%;background:#fff;display:flex;align-items:center;justify-content:center}
.hero-title{left:96px;top:432px;font-size:76px;font-weight:600;color:#fff;line-height:1.1}

/* welcome */
.photo{background:
    radial-gradient(ellipse 200px 160px at 30% 60%,rgba(235,228,215,.9),transparent 70%),
    radial-gradient(ellipse 180px 220px at 80% 45%,rgba(70,78,88,.55),transparent 70%),
    linear-gradient(125deg,#d9dcdf 0%,#a9aeb3 40%,#eceded 70%,#7f868d 100%)}
.card{background:#fff;border-radius:8px;box-shadow:0 6px 28px rgba(0,0,0,.08)}
.welcome-card{left:576px;top:912px;width:524px;height:357px;padding:44px 29px}
.kicker{border-left:4px solid var(--blue);padding-left:10px}
.kicker .small{display:block;font-size:27px;font-weight:500;color:var(--blue);line-height:1.1}
.kicker .big{display:block;font-size:54px;font-weight:500;color:var(--ink);line-height:1.05}
.welcome-card p{font-size:14.5px;line-height:30px;text-align:justify;margin-top:18px;color:var(--text)}

/* custom software band */
.band{left:0;top:1407px;width:1200px;height:562px;background:
    radial-gradient(ellipse 360px 300px at 72% 45%,rgba(214,170,120,.55),transparent 70%),
    radial-gradient(ellipse 260px 320px at 92% 55%,rgba(40,95,110,.55),transparent 70%),
    linear-gradient(90deg,#1f1c18 0%,#3d3327 35%,#6f5c43 58%,#4b4a42 78%,#1e2a30 100%)}
.band::before{content:"";position:absolute;inset:0;background:linear-gradient(90deg,rgba(0,0,0,.45),rgba(0,0,0,0) 55%)}
.band-title{left:96px;top:1518px;font-size:47px;font-weight:600;color:#fff;line-height:44px}
.band-text{left:104px;top:1633px;width:441px;font-size:14.5px;line-height:30px;color:#fff;text-align:justify}

/* blog */
.blog{left:0;top:1969px;width:1200px;height:750px;background:var(--pale)}
.blog-heading{left:0;top:2045px;width:1200px;text-align:center;font-size:47px;font-weight:600;color:var(--ink)}
.post-meta{font-size:12px;color:var(--blue)}
.post-title{font-size:21px;font-weight:500;color:var(--ink);line-height:28px;margin-top:6px}
.post-text{font-size:13px;line-height:23px;color:var(--text);margin-top:6px}
.post-link{font-size:14px;font-weight:600;color:var(--blue);margin-top:12px;display:flex;align-items:center;gap:4px}
.post-big{left:100px;top:2138px;width:473px;height:487px;overflow:hidden}
.post-big .body{padding:14px 18px}
.post-side{left:608px;width:480px;height:223px;overflow:hidden;display:flex}
.post-side .thumb{position:relative;width:179px;height:223px;flex:none}
.post-side .body{padding:32px 14px 0 21px}
.post-side .post-title{font-size:19px;line-height:27px}
.img-office{position:relative;height:280px;background:
    radial-gradient(ellipse 140px 120px at 45% 45%,rgba(90,150,190,.55),transparent 70%),
    radial-gradient(ellipse 220px 90px at 50% 85%,rgba(150,110,70,.7),transparent 70%),
    linear-gradient(135deg,#4e5a60 0%,#8e8a7c 45%,#c9c4b6 70%,#3a454c 100%)}
.img-chart{background:
    radial-gradient(ellipse 90px 60px at 60% 45%,rgba(230,170,60,.35),transparent 70%),
    linear-gradient(140deg,#151c27 0%,#2f3a4a 55%,#1d2530 100%)}
.img-hourglass{background:
    radial-gradient(ellipse 80px 120px at 55% 50%,rgba(250,200,110,.75),transparent 70%),
    linear-gradient(170deg,#2a1e14 0%,#7a4f22 45%,#d59645 80%,#f0b860 100%)}

/* signup */
.signup{left:0;top:2719px;width:1200px;height:124px;background:var(--blue)}
.signup h3{position:absolute;left:99px;top:28px;font-size:29px;font-weight:600;color:#fff}
.signup p{position:absolute;left:100px;top:72px;font-size:12px;color:#fff}
.signup-form{left:556px;top:38px;width:531px;height:48px;border:2px solid #fff;border-radius:6px;background:#fff;display:flex;overflow:hidden}
.signup-form .field{flex:1;font-size:13px;color:var(--text);line-height:44px;padding-left:13px}
.signup-form .submit{width:136px;background:var(--blue);color:#fff;font-weight:600;font-size:16px;text-align:center;line-height:44px}

/* footer */
.footer{left:0;top:2843px;width:1200px;height:388px;background:var(--footer);color:#fff}
.footer .brand{color:#fff;font-size:30px}
.footer .brand .mark{width:44px;height:44px}
.f-about{left:100px;top:184px;width:280px;font-size:13px;line-height:23px}
.f-head{font-size:19px;font-weight:600;text-decoration:underline;text-underline-offset:5px}
.f-list{list-style:none;font-size:16px;line-height:33px;margin-top:14px}
.f-contact{list-style:none;font-size:16px;line-height:26px;margin-top:16px}
.f-contact li{display:flex;gap:12px;margin-bottom:10px}
.socials{display:flex;gap:9px;margin-top:16px}
.socials span{width:31px;height:31px;border:1.5px solid #fff;border-radius:50%}
.f-rule{left:100px;top:326px;width:1000px;height:1px;background:#333}
.f-bottom{top:347px;font-size:13px}
.to-top{left:1124px;top:302px;width:50px;height:50px;border-radius:50%;background:#fff;border:4px solid #888;display:flex;align-items:center;justify-content:center}
</style>
</head>
<body>

<!-- top bar -->
<div class="abs topbar">
  <div class="abs search">Search
    <svg width="15" height="15" viewBox="0 0 15 15" fill="none" stroke="#dcefff" stroke-width="1.5"><circle cx="6" cy="6" r="4.5"/><line x1="9.5" y1="9.5" x2="13.5" y2="13.5"/></svg>
  </div>
  <div class="abs sep" style="left:735px"></div>
  <div class="abs top-contact" style="left:750px">
    <svg width="17" height="17" viewBox="0 0 24 24" fill="#fff"><path d="M6.6 10.8a15 15 0 0 0 6.6 6.6l2.2-2.2a1 1 0 0 1 1-.25 11.4 11.4 0 0 0 3.6.57 1 1 0 0 1 1 1V20a1 1 0 0 1-1 1A17 17 0 0 1 3 4a1 1 0 0 1 1-1h3.5a1 1 0 0 1 1 1c0 1.25.2 2.450.57 3.57a1 1 0 0 1-.25 1z"/></svg>
    +61 400 555 218
  </div>
  <div class="abs sep" style="left:896px"></div>
  <div class="abs top-contact" style="left:909px">
    <svg width="18" height="14" viewBox="0 0 18 14" fill="none" stroke="#fff" stroke-width="1.5"><rect x="1" y="1" width="16" height="12"/><path d="M1 1l8 7 8-7"/></svg>
    mara@quillabend.com
  </div>
</div>

<!-- navigation -->
<header class="abs nav">
  <div class="abs brand" style="left:100px;top:20px"><span class="mark"></span>Quillabend</div>
  <nav class="abs menu" style="left:0;width:1200px">
    <a class="item active" style="left:397px">HOME</a>
    <a class="item" style="left:484px">SERVICES</a>
    <a class="item" style="left:597px">ABOUT</a>
    <a class="item" style="left:691px">BLOG</a>
    <a class="item" style="left:774px">CONTACT</a>
  </nav>
  <a class="abs btn" style="left:874px;top:21px;width:99px;height:34px">LOG IN <span class="arrow" style="background:#fff"></span></a>
  <a class="abs btn btn-outline" style="left:981px;top:21px;width:118px;height:34px">REGISTER <span class="arrow"></span></a>
</header>

<!-- hero -->
<section class="abs hero media" role="img" aria-label="Background video of a surgical team with a robotic arm and holographic medical display"></section>
<div class="abs play"><div class="inner"><svg width="24" height="26" viewBox="0 0 24 26"><path d="M3 2l19 11L3 24z" fill="var(--blue)"/></svg></div></div>
<h1 class="abs hero-title">Quillabend</h1>
<a class="abs btn" style="left:98px;top:532px;width:199px;height:39px">FREE EMAIL COURSE <span class="arrow" style="background:#fff"></span></a>

<!-- welcome -->
<div class="abs photo media" style="left:100px;top:868px;width:524px;height:445px" role="img" aria-label="Photo of developers working together at computers in an office"></div>
<div class="abs card welcome-card">
  <div class="kicker"><span class="small">Welcome to</span><span class="big">Quillabend</span></div>
  <p>Quillabend’ mission is to provide a custom software development service across a range of technologies by using best practice agile methodologies and tools to deliver customer value on time and within budget.</p>
  <a class="btn" style="width:157px;height:41px;margin-top:16px">LEARN MORE <span class="arrow" style="background:#fff"></span></a>
</div>

<!-- custom software development -->
<section class="abs band media" role="img" aria-label="Photo of two colleagues reviewing documents at a screen"></section>
<h2 class="abs band-title">Custom Software<br>Development</h2>
<p class="abs band-text">Using carefully selected software tools and carefully designed custom applications can make running your business so much more enjoyable. Quillabend can provide an upfront quote and regular progress updates on your project to give you piece of mind.</p>
<a class="abs btn" style="left:105px;top:1811px;width:156px;height:40px">LEARN MORE <span class="arrow" style="background:#fff"></span></a>

<!-- blog -->
<section class="abs blog"></section>
<h2 class="abs blog-heading">Our Latest Blog</h2>

<article class="abs card post-big">
  <div class="img-office media" role="img" aria-label="Photo of a man using a tablet at a desk"></div>
  <div class="body">
    <div class="post-meta">10 April 2022 by maralw</div>
    <h3 class="post-title">What makes a GREAT web application?</h3>
    <p class="post-text">So you’re looking to create a new web application. You’ll need to consider the budget, the requirements of your business and the functions you want the web application to perform for you.</p>
    <a class="post-link">LEARN MORE <span class="arrow"></span></a>
  </div>
</article>

<article class="abs card post-side" style="top:2138px">
  <div class="thumb img-chart media" role="img" aria-label="Illustration of a hand touching a rising line chart"></div>
  <div class="body">
    <div class="post-meta">10 April 2022 by maralw</div>
    <h3 class="post-title">The Absolutely Unbeatable Way Of Estimating...</h3>
    <p class="post-text" style="margin-top:8px">Successful projects require accurate es-timates of the effort required</p>
    <a class="post-link" style="margin-top:10px">LEARN MORE <span class="arrow"></span></a>
  </div>
</article>

<article class="abs card post-side" style="top:2398px">
  <div class="thumb img-hourglass media" role="img" aria-label="Photo of an hourglass on a hand at sunset"></div>
  <div class="body">
    <div class="post-meta">1 July 2020 by maralw</div>
    <h3 class="post-title">Making the most of your time investment</h3>
    <p class="post-text" style="margin-top:8px">1. First Generation – Classic Time Management Classic</p>
    <a class="post-link" style="margin-top:10px">LEARN MORE <span class="arrow"></span></a>
  </div>
</article>

<!-- signup -->
<section class="abs signup">
  <h3>Sign up for Clearpath Insights</h3>
  <p>At vero eos et accusamus et iusto odio dignissimos ducimus</p>
  <div class="abs signup-form"><span class="field">Enter email address</span><span class="submit">SUBMIT</span></div>
</section>

<!-- footer -->
<footer class="abs footer">
  <div class="abs brand" style="left:100px;top:100px"><span class="mark"></span>Quillabend</div>
  <p class="abs f-about">Quillabend was founded in 1998. We have helped many customers achieve their dreams.</p>

  <div class="abs" style="left:449px;top:92px">
    <div class="f-head">Quick Links</div>
    <ul class="f-list"><li>Home</li><li>Services</li><li>About</li><li>Contact</li><li>Blog</li></ul>
  </div>

  <div class="abs" style="left:627px;top:92px">
    <div class="f-head">Contact Info</div>
    <ul class="f-contact">
      <li><svg width="18" height="22" viewBox="0 0 18 22" fill="#fff"><path d="M9 0a8 8 0 0 0-8 8c0 6 8 14 8 14s8-8 8-14a8 8 0 0 0-8-8zm0 11a3 3 0 1 1 0-6 3 3 0 0 1 0 6z"/></svg><span>17 Harbourline Road<br>Westmere Queensland 4210<br>Australia</span></li>
      <li><svg width="18" height="18" viewBox="0 0 24 24" fill="none" stroke="#fff" stroke-width="1.8"><path d="M6.6 10.8a15 15 0 0 0 6.6 6.6l2.2-2.2a1 1 0 0 1 1-.25 11.4 11.4 0 0 0 3.6.57 1 1 0 0 1 1 1V20a1 1 0 0 1-1 1A17 17 0 0 1 3 4a1 1 0 0 1 1-1h3.5a1 1 0 0 1 1 1c0 1.25.2 2.45.57 3.57a1 1 0 0 1-.25 1z"/></svg><span>Phone: +61 400 555 218</span></li>
      <li><svg width="19" height="14" viewBox="0 0 18 14" fill="none" stroke="#fff" stroke-width="1.5" style="margin-top:6px"><rect x="1" y="1" width="16" height="12"/><path d="M1 1l8 7 8-7"/></svg><span>Email: mara@quillabend.com</span></li>
    </ul>
  </div>

  <div class="abs" style="left:948px;top:92px">
    <div class="f-head">Find Us Online</div>
    <div class="socials" aria-label="Social profiles"><span></span><span></span><span></span><span></span></div>
  </div>

  <div class="abs f-rule"></div>
  <div class="abs f-bottom" style="left:100px">©Copyright ©2022 quillabend. All Rights Reserved.</div>
  <div class="abs f-bottom" style="left:892px">Privacy Policy | Terms of Service</div>
  <div class="abs to-top"><svg width="22" height="12" viewBox="0 0 22 12" fill="none" stroke="var(--blue)" stroke-width="2"><path d="M1 11L11 1l10 10"/></svg></div>
</footer>

</body>
</html>
```